CD/Album cover design - Ember & Tide

Hi, I need an album cover designed. The name of the album is called 'Ember and Tide' Not 100% sure of the concept, but using colored lines, Geometrical shapes etc, angles and maybe a circle or triangle in the middle. A cross between, Velvet Harbor ,Hollow rim of the sea (But dont make it look like this old look album) , 80s retro synthwave album covers, perhaps with neon color lines but not all of it etc. Have it modern looking . My name on cover and album name. Back, songs etc and info details. The style of the music is EDM meets guitar. Trap, house music and guitar as the main theme instrument, with sythns. Keep it relatively simple looking, and maybe have the background white,, but with the color designs, wording etc colors. or if you feel it would look better another way, just use your own judgement and creativity. Ve attached a couple of Pics. The Velvet Harbor pic , more of concept. The retro one... I like the design in the middle but not wording at the top. The QX rise one, I like how the wording is in the middle of circle. So a combination of these, with geometrical lines, colors, etc. I am also open to a completely new idea that you think would look awesome. The album is really combining Guitar with House/Tap EDM music, and the concept Ember and Tide - The beginning and end (Of everything) Thanks
EDM , Guitarists
Music, EDM, Guitar Instrumental

```html
<!DOCTYPE html>
<html lang="en">
<head>
<meta charset="utf-8">
<title>Ember and Tide — Album Cover</title>
<link rel="stylesheet" href="https://fonts.googleapis.com/css2?family=Orbitron:wght@600;700&display=swap">
<style>
  :root {
    --night: #0b0a2a;
    --night-deep: #05041a;
    --indigo: #2a1f7a;
    --violet: #7a2fd6;
    --magenta: #e03aa8;
    --azure: #2f7cf0;
    --core: #050418;
    --title-cyan: #33f0f2;
    --title-glow: rgba(51, 240, 242, 0.75);
    --subtitle-orange: #f2642a;
  }

  * { margin: 0; padding: 0; box-sizing: border-box; }

  html, body {
    width: 1200px;
    height: 1200px;
    overflow: hidden;
    background: var(--night-deep);
  }

  .album-cover {
    position: relative;
    width: 1200px;
    height: 1200px;
    background:
      radial-gradient(circle at 20% 25%, rgba(122, 47, 214, 0.25), transparent 40%),
      radial-gradient(circle at 85% 80%, rgba(47, 124, 240, 0.18), transparent 45%),
      linear-gradient(160deg, var(--night) 0%, var(--night-deep) 100%);
    overflow: hidden;
  }

  .sound-burst {
    position: absolute;
    left: 60px;
    top: 87px;
    width: 1000px;
    height: 1000px;
  }

  .title-block {
    position: absolute;
    left: 560px;
    top: 587px;
    transform: translate(-50%, -50%);
    text-align: center;
    font-family: "Orbitron", sans-serif;
  }

  .album-title {
    display: block;
    font-weight: 700;
    font-size: 96px;
    letter-spacing: 4px;
    line-height: 1;
    color: var(--title-cyan);
    text-shadow: 0 0 12px var(--title-glow), 0 0 28px var(--title-glow);
  }

  .album-subtitle {
    display: block;
    margin-top: 40px;
    font-weight: 600;
    font-size: 66px;
    letter-spacing: 6px;
    line-height: 1;
    color: var(--subtitle-orange);
  }
</style>
</head>
<body>
  <main class="album-cover">
    <svg class="sound-burst" viewBox="0 0 1000 1000" role="img"
         aria-label="Circular neon burst of pixel rings and floating music notes in blue, violet and pink">
      <defs>
        <radialGradient id="burst-glow" cx="50%" cy="50%" r="50%">
          <stop offset="0%" stop-color="var(--core)"/>
          <stop offset="40%" stop-color="var(--core)"/>
          <stop offset="46%" stop-color="var(--azure)" stop-opacity="0.9"/>
          <stop offset="62%" stop-color="var(--violet)" stop-opacity="0.85"/>
          <stop offset="78%" stop-color="var(--magenta)" stop-opacity="0.55"/>
          <stop offset="100%" stop-color="var(--indigo)" stop-opacity="0"/>
        </radialGradient>
      </defs>
      <circle cx="500" cy="500" r="500" fill="url(#burst-glow)"/>
    </svg>

    <h1 class="title-block">
      <span class="album-title">EMBER</span>
      <span class="album-subtitle">TIDE</span>
    </h1>
  </main>
</body>
</html>
```